POLITICAL CARD TO HAND OUT

A LITTLE LARGER THAN THE REGULAR BUSINESS CARD WITH THE ABOVE INFORMATION.

Industry/Entity Type

Business

Contact Information for Business Card

ELECT *DEAN HOLT* FOR JUSTICE OF THE PEACE PCT 6-EXPERIENCED LEADERSHIP- WITH MY PICTURE ON IT- PHONE 347-610-2853-MERIDIAN PRIMARY - EARLY VOTING FEB 18TH THRU FEB 28 AND ELECTION DAY IS MARCH 4TH, 2014- USE RED WHITE AND BLUE WITH SOME STARS.

Requirements
Must have
• A FIVE POINTED STAR ON EACH SIDE OF MY NAME

```html
<!DOCTYPE html>
<html lang="en">
<head>
<meta charset="utf-8">
<title>Elect Dean Holt – Justice of the Peace</title>
<link rel="stylesheet" href="https://fonts.googleapis.com/css2?family=Alfa+Slab+One&family=Archivo+Black&display=swap">
<style>
  :root {
    --navy: #1b2a5e;
    --red: #e2232b;
    --white: #ffffff;
    --gold: #f2c21b;
    --gold-deep: #e3a20f;
  }
  html, body {
    margin: 0;
    padding: 0;
    width: 1200px;
    height: 772px;
    overflow: hidden;
    background: var(--white);
  }
  .card {
    position: relative;
    width: 1200px;
    height: 772px;
    overflow: hidden;
    background: var(--white);
    font-family: "Archivo Black", "Arial Black", sans-serif;
  }
  .card__layer {
    position: absolute;
    inset: 0;
  }
  .candidate-photo {
    position: absolute;
    left: 0;
    top: 93px;
    width: 400px;
    height: 543px;
    background: linear-gradient(165deg, #e9e2d6 0%, #b9a58a 40%, #2a2630 100%);
  }
  .justice-emblem {
    position: absolute;
    left: 822px;
    top: 276px;
    width: 190px;
    height: 92px;
    background: linear-gradient(90deg, var(--gold) 0%, var(--gold-deep) 100%);
    border-radius: 8px;
    opacity: 0.85;
  }
  .headline {
    position: absolute;
    left: 360px;
    top: 2px;
    width: 805px;
    margin: 0;
    display: flex;
    justify-content: space-between;
    font-family: "Alfa Slab One", Georgia, serif;
    font-weight: 400;
    font-size: 132px;
    line-height: 1;
    color: var(--red);
    text-shadow:
      -3px -3px 0 var(--white), 3px -3px 0 var(--white),
      -3px 3px 0 var(--white), 3px 3px 0 var(--white),
      0 -3px 0 var(--white), 0 3px 0 var(--white),
      -3px 0 0 var(--white), 3px 0 0 var(--white),
      7px 6px 0 rgba(0,0,0,0.35);
  }
  .office {
    position: absolute;
    left: 411px;
    width: 770px;
    margin: 0;
    text-align: center;
    color: var(--red);
    line-height: 1;
    white-space: nowrap;
  }
  .office--title {
    top: 186px;
    font-size: 33px;
  }
  .office--tagline {
    top: 234px;
    font-size: 38px;
    letter-spacing: -0.5px;
  }
  .candidate-name {
    position: absolute;
    left: 462px;
    top: 398px;
    margin: 0;
    font-family: "Alfa Slab One", Georgia, serif;
    font-weight: 400;
    line-height: 1;
    white-space: nowrap;
    transform: rotate(-2deg);
    transform-origin: left bottom;
  }
  .candidate-name__first {
    color: var(--red);
    font-size: 110px;
    text-shadow: 5px 5px 0 rgba(0,0,0,0.25);
  }
  .candidate-name__last {
    color: var(--navy);
    font-size: 98px;
    margin-left: 16px;
    text-shadow: 4px 4px 0 rgba(0,0,0,0.2);
  }
  .contact {
    position: absolute;
    left: 0;
    top: 652px;
    width: 1200px;
    margin: 0;
    text-align: center;
    color: var(--navy);
    font-size: 47px;
    line-height: 1;
    white-space: nowrap;
    transform: rotate(-0.6deg);
  }
  .voting-dates {
    position: absolute;
    left: 0;
    top: 740px;
    width: 1200px;
    margin: 0;
    text-align: center;
    color: var(--white);
    font-size: 20px;
    line-height: 1;
    white-space: nowrap;
  }
</style>
</head>
<body>
  <main class="card">
    <svg class="card__layer" width="1200" height="772" viewBox="0 0 1200 772" aria-hidden="true">
      <defs>
        <polygon id="star" points="0,-1 0.2245,-0.309 0.951,-0.309 0.363,0.118 0.588,0.809 0,0.382 -0.588,0.809 -0.363,0.118 -0.951,-0.309 -0.2245,-0.309"/>
      </defs>
      <polygon points="0,0 1200,0 1200,132 0,143" fill="var(--navy)"/>
      <polygon points="0,560 1200,481 1200,772 0,772" fill="var(--navy)"/>
      <polygon points="0,636 1200,613 1200,714 0,733" fill="var(--white)"/>
      <g fill="var(--white)">
        <use href="#star" transform="translate(500 590) scale(19)"/>
        <use href="#star" transform="translate(590 586) scale(22)"/>
        <use href="#star" transform="translate(711 581) scale(25)"/>
        <use href="#star" transform="translate(846 570) scale(28)"/>
        <use href="#star" transform="translate(986 558) scale(32)"/>
        <use href="#star" transform="translate(1145 549) scale(35)"/>
      </g>
    </svg>

    <div class="candidate-photo" role="img" aria-label="Portrait photo of the candidate in a white cowboy hat, dark suit and patterned tie"></div>
    <div class="justice-emblem" role="img" aria-label="Gold illustration of Lady Justice holding the scales"></div>

    <h1 class="headline"><span>E</span><span>L</span><span>E</span><span>C</span><span>T</span></h1>

    <p class="office office--title">FOR JUSTICE OF THE PEACE</p>
    <p class="office office--tagline">PCT 6-EXPERIENCED LEADERSHIP</p>

    <svg class="card__layer" width="1200" height="772" viewBox="0 0 1200 772" aria-hidden="true">
      <g fill="var(--gold)">
        <use href="#star" transform="translate(426 386) scale(20)"/>
        <use href="#star" transform="translate(1043 311) scale(14)"/>
        <use href="#star" transform="translate(1103 318) scale(17)"/>
        <use href="#star" transform="translate(1162 346) scale(21)"/>
      </g>
    </svg>

    <h2 class="candidate-name">
      <span class="candidate-name__first">DEAN</span><span class="candidate-name__last">HOLT</span>
    </h2>

    <p class="contact">PHONE 347-610-2853-MERIDIAN PRIMARY</p>
    <p class="voting-dates">EARLY VOTING FEB 18TH THRU FEB 28 · ELECTION DAY MARCH 4TH, 2014</p>
  </main>
</body>
</html>
```